Business Card and Letterhead for Juniper Anvil - (Have Logo)

Update 4: Removed company reg no from business card details as it looked a bit out of place. Updated services list.
UPDATE 3
Sorry, I got the address a little bit wrong, have updated it below. Sorry for any inconvenience caused.
UPDATE 2
Finally I have the details for the business cards and letterhead. Submissions already made do not have to be updated unless shortlisted, if all new submissions could include the details for me, Marcus, that would be very much appreciated and help with the final shortlist selection. I intend to share a shortlist of the three best entries with past and existing customers for their feedback and opinions. Thank you all again for your time.
Here are the details.
Marcus Telby
Web Developer
T: 01632 960 418
E: marcus@juniperanvil.example
www.juniperanvil.example
Professional Photography
Web Solutions & E-Commerce
Audio & HD Video Production
Marketing & Promotions
Identity and Branding
Juniper Anvil Ltd
Suite 20938, 3rd Floor
212-224 Orchard Lane
London, N7 9QX
Company Reg. No: 05829147
The order and the layout of the information are of course down to the design, but the company registration number should be smaller and less prominent. The formatting of the telephone and email address using a T: and an E: I am not sure about and again if it is Tel: or Email: or Icons is up to the design.
The Company No. on the letterhead should read (somewhere in small text along the bottom):
Juniper Anvil is a Ltd Company registered in England & Wales, Registration No. 05829147.
The second business card details are
Oliver Brackley
Photographer
T: 01632 960 418
E: oliver@juniperanvil.example
Everything else the same of course.
Thank you again for all the submissions so far.
END OF UPDATE 2
-
UPDATE 1: Please do not alter the logo nor the logo colours. (This was a previous pixel forum project and I am extremely happy with it. The icon can stand alone of course, but I have had to eliminate all entries that have made it black and white, or reversed the icon.) I would like to thank everyone that has participated so far and am very grateful for all your thought and time.
End of Update 1
-
Original Brief:
I have attached the logo vector file.
Following a superb logo from a previous Pixel Forum project I am now looking for a business card design and (although less important) a letterhead as well.
I must admit I tried to do it myself but could only come up with the usual amateur stuff that in comparison to the quality of the logo looked awful.
About Us
Juniper Anvil Ltd will be a new company due to start in January. It is really just me (a web developer) and my friend (a photographer). We will be aiming at the usual small to medium sized businesses in the local area, selling various digital services including photographic services to the public, web hosting and development, commercial photography, modelling services (not us!), full video and film production and possibly a bit of marketing as well. (Really it is anything we can do professionally all lumped together! We met running seperate businesses which have both since closed)
We will not be competing on price. We plan to be expensive but fair. Certainly not the cheapest.
What we are looking for
Business Card
I imagine a double sided business card, which will be used for more than one person. I imagine the front to be the same for everyone and the persons details to be on the back, although this is of course only my thoughts and I am of course completely open to any ideas.
The card could also have a services list or a bit about what we do on it. It might feature the website address, our business address (mail forwarding address) or our registered company number.
Or it might have none of that, we are completely open to any ideas and have no real fixed opinions. I just want it to be really nice :-)
Letterhead (secondary importance)
We will make our decision primarily on the business card, although a mathcing letterhead would be fantastic. Something standardish in format and simple, although again, all ideas are welcomed.
I hope that is enough information but if you have any questions I will answer them as fully and as quickly as possible.
Thank you once again and I really look forward to seeing your ideas and picking a winner.
Marcus T.
Small businesses AND the general public
Film Production

```html
<!DOCTYPE html>
<html lang="en">
<head>
<meta charset="utf-8">
<title>Juniper Anvil — Business Card</title>
<link rel="stylesheet" href="https://fonts.googleapis.com/css2?family=Jost:wght@400;500;600&family=Bowlby+One+SC&display=swap">
<style>
  :root {
    --bg: #e9e6e2;
    --metal-light: #eeeeee;
    --metal-mid: #d9d9d9;
    --metal-dark: #c4c4c4;
    --ink: #1c1c1c;
    --ink-soft: #3a3a3a;
    --brand-red: #b3262a;
    --paper: #ffffff;
  }
  * { box-sizing: border-box; margin: 0; padding: 0; }
  html, body { width: 1200px; height: 900px; overflow: hidden; }
  body {
    background: var(--bg);
    font-family: "Jost", "Futura", sans-serif;
    color: var(--ink);
  }
  .canvas {
    position: relative;
    width: 1200px;
    height: 900px;
    display: flex;
    align-items: center;
    justify-content: center;
    gap: 90px;
  }
  .card {
    position: relative;
    background: linear-gradient(135deg, var(--metal-light) 0%, var(--metal-mid) 45%, var(--metal-light) 70%, var(--metal-dark) 100%);
    box-shadow: 0 10px 30px rgba(0,0,0,.18);
    overflow: hidden;
  }

  /* Front */
  .card-front {
    width: 560px;
    height: 320px;
    display: flex;
    flex-direction: column;
    align-items: center;
    justify-content: center;
  }
  .brand {
    display: flex;
    align-items: center;
    gap: 16px;
  }
  .brand-mark {
    width: 44px;
    height: 44px;
    background: var(--brand-red);
  }
  .brand-name {
    font-weight: 600;
    font-size: 46px;
    letter-spacing: 3px;
    color: var(--ink-soft);
    text-transform: uppercase;
    line-height: 1;
  }
  .tagline {
    margin-top: 18px;
    font-size: 15px;
    font-weight: 500;
    letter-spacing: 1.4px;
    text-transform: uppercase;
    color: var(--ink);
  }

  /* Back */
  .card-back {
    width: 320px;
    height: 560px;
    padding-top: 52px;
    display: flex;
    flex-direction: column;
    align-items: center;
  }
  .person-name {
    font-family: "Bowlby One SC", "Impact", sans-serif;
    font-size: 28px;
    letter-spacing: 1.5px;
    color: var(--ink);
    line-height: 1;
  }
  .person-role {
    margin-top: 6px;
    font-size: 15px;
    letter-spacing: 1px;
    color: var(--brand-red);
    text-transform: uppercase;
  }
  .contact {
    margin-top: 14px;
    display: flex;
    flex-direction: column;
    align-items: center;
    gap: 7px;
    font-size: 12.5px;
    letter-spacing: .6px;
    color: var(--brand-red);
    text-transform: uppercase;
  }
  .contact-icon { width: 18px; height: 18px; display: block; }
  .photo-panel {
    position: absolute;
    left: 22px;
    right: 22px;
    bottom: 24px;
    height: 250px;
    display: flex;
  }
  .photo-tab {
    width: 34px;
    background: var(--ink);
    border-radius: 10px 0 0 10px;
    position: relative;
  }
  .photo-tab-label {
    position: absolute;
    left: 50%;
    top: 88px;
    transform: translate(-50%, -50%) rotate(-90deg);
    color: var(--paper);
    font-size: 11px;
    letter-spacing: 1px;
    text-transform: uppercase;
    white-space: nowrap;
  }
  .photo-tab-icon {
    position: absolute;
    left: 8px;
    bottom: 12px;
    width: 18px;
    height: 18px;
  }
  .photo-area {
    flex: 1;
    background: var(--paper);
    border-radius: 0 14px 14px 0;
    box-shadow: inset 0 0 6px rgba(0,0,0,.08);
  }
</style>
</head>
<body>
<main class="canvas">

  <section class="card card-front" aria-label="Business card front">
    <div class="brand">
      <span class="brand-mark"></span>
      <span class="brand-name">Juniper Anvil</span>
    </div>
    <p class="tagline">Web Solutions + Photography + Video Production</p>
  </section>

  <section class="card card-back" aria-label="Business card back">
    <h1 class="person-name">JOHN JUNIPER</h1>
    <p class="person-role">Web Developer</p>
    <div class="contact">
      <span>yourname@juniperanvil.example</span>
      <svg class="contact-icon" viewBox="0 0 20 20" aria-hidden="true">
        <rect x="2" y="4" width="16" height="12" fill="#1c1c1c"/>
        <path d="M2 4 L10 11 L18 4" fill="none" stroke="#e6e6e6" stroke-width="1.4"/>
      </svg>
      <svg class="contact-icon" viewBox="0 0 20 20" aria-hidden="true">
        <path d="M4 6 Q10 2 16 6 L15 8 L12 7 L12 9 L8 9 L8 7 L5 8 Z" fill="#1c1c1c"/>
        <rect x="5" y="10" width="10" height="7" rx="1" fill="#1c1c1c"/>
        <circle cx="10" cy="13.5" r="1.8" fill="#e6e6e6"/>
      </svg>
      <span>555 014 273 1</span>
      <span>www.juniperanvil.example</span>
      <svg class="contact-icon" viewBox="0 0 20 20" aria-hidden="true">
        <circle cx="10" cy="10" r="8" fill="none" stroke="#1c1c1c" stroke-width="1.6"/>
        <ellipse cx="10" cy="10" rx="3.5" ry="8" fill="none" stroke="#1c1c1c" stroke-width="1.3"/>
        <line x1="2" y1="10" x2="18" y2="10" stroke="#1c1c1c" stroke-width="1.3"/>
      </svg>
      <span>London UK</span>
    </div>

    <div class="photo-panel">
      <div class="photo-tab">
        <span class="photo-tab-label">juniperanvil</span>
        <svg class="photo-tab-icon" viewBox="0 0 20 20" aria-hidden="true">
          <path d="M4 16 L5 12 L13 4 L16 7 L8 15 Z" fill="none" stroke="#ffffff" stroke-width="1.5" stroke-linejoin="round"/>
        </svg>
      </div>
      <div class="photo-area"></div>
    </div>
  </section>

</main>
</body>
</html>
```